TELVORA needs three flags/signs to celebrate green buildings

The template for the flag is in the attachments, and can be found on

We are looking to celebrate three of Australia's most energy efficient buildings by creating some signage for them to display. One will be an office building, one a hotel, one a shopping centre. They should include the words: "You are entering Australia's most energy efficient office/hotel/shopping centre".

So to clarify, there will need to be three different designs (office/hotel/shopping centre) but each design will need consider two sides of the flag.
Updates

Thanks to everyone who submitted a design. I have already given feedback to most. I will provide feedback to those I haven't by the end of the day. We received 30 designs all up, over half were good quality and some were very good quality. Today I'll put my favourites through to our wider team for a poll. Many thanks once again.

Target Market(s)

People entering the buildings

Industry/Entity Type

Property Management

Font styles to use
Other font styles liked:
• see logo guidelines

Requirements
Must have
• The TELVORA logo.
• The wording "You are entering Australia's most energy efficient office/hotel/shopping centre."
• It should fit into the 'flapterns' templates provided.
• The designs should refer to the TELVORA logo guidelines for style / font.
• Note: we use a seven pointed star.
Nice to have
• We have two elements that we use frequently: stars and a 'wave'. See examples of documents for ideas.
• The final design should communicate celebration with corporate elegance.

```html
<!DOCTYPE html>
<html lang="en">
<head>
<meta charset="utf-8">
<title>TELVORA energy efficient building flags</title>
<link rel="stylesheet" href="https://fonts.googleapis.com/css2?family=Arimo:wght@700&display=swap">
<style>
  :root {
    --canvas: #ffffff;
    --text: #ffffff;
    --edge: #2a2a3a;
    --curve: #1a1a1a;
    --office-top: #7fd4f5;
    --office-mid: #1e8fd8;
    --office-low: #173f9c;
    --office-icon: #1f8ad6;
    --shop-top: #f7a325;
    --shop-mid: #f6b531;
    --shop-low: #e9781c;
    --shop-icon: #f3a21f;
    --hotel-top: #28204e;
    --hotel-mid: #3b2a6a;
    --hotel-edge: #e02a52;
    --hotel-icon: #e8407e;
  }
  * { margin: 0; padding: 0; box-sizing: border-box; }
  html, body { width: 784px; height: 1200px; overflow: hidden; background: var(--canvas); }
  .canvas { position: relative; width: 784px; height: 1200px; }
  .flag {
    position: absolute;
    top: 13px;
    width: 236px;
    height: 1167px;
    border: 1px solid var(--edge);
    overflow: hidden;
    font-family: "Arimo", Arial, sans-serif;
    color: var(--text);
  }
  .flag--office { left: 18px; }
  .flag--shopping { left: 274px; }
  .flag--hotel { left: 530px; }
  .flag__backdrop { position: absolute; inset: 0; }
  .flag--office .flag__backdrop {
    background:
      radial-gradient(ellipse 80% 30% at 70% 22%, rgba(255,255,255,.45), transparent 70%),
      linear-gradient(180deg, var(--office-top) 0%, var(--office-mid) 45%, var(--office-low) 100%);
  }
  .flag--shopping .flag__backdrop {
    background:
      radial-gradient(ellipse 70% 35% at 40% 60%, rgba(255,240,180,.5), transparent 70%),
      linear-gradient(180deg, var(--shop-top) 0%, var(--shop-mid) 45%, var(--shop-low) 100%);
  }
  .flag--hotel .flag__backdrop {
    background:
      radial-gradient(ellipse 60% 30% at 75% 30%, rgba(230,200,255,.45), transparent 70%),
      linear-gradient(90deg, var(--hotel-top) 0%, var(--hotel-mid) 60%, var(--hotel-edge) 100%);
  }
  .flag__curve { position: absolute; inset: 0; }
  .flag__message {
    position: absolute;
    top: 262px;
    left: 26px;
    right: 14px;
    font-size: 28px;
    line-height: 1.24;
    font-weight: 700;
  }
  .flag__icon {
    position: absolute;
    top: 782px;
    left: 50%;
    transform: translateX(-50%);
    width: 96px;
    height: 104px;
  }
  .flag__brand {
    position: absolute;
    left: 26px;
    bottom: 48px;
    display: flex;
    align-items: center;
    gap: 10px;
    font-size: 27px;
    font-weight: 700;
    letter-spacing: 1px;
  }
  .flag__brand-dot { width: 22px; height: 22px; border-radius: 50%; background: var(--text); }
</style>
</head>
<body>
<main class="canvas">

  <section class="flag flag--office">
    <div class="flag__backdrop" role="img" aria-label="Abstract blue light waves background"></div>
    <svg class="flag__curve" viewBox="0 0 236 1167"><path d="M26 300 Q34 50 200 0" fill="none" stroke="var(--curve)" stroke-width="2"/></svg>
    <p class="flag__message">You are<br>entering<br>Australia's<br>most<br>energy<br>efficient<br>office.</p>
    <svg class="flag__icon" viewBox="0 0 96 104">
      <path d="M48 2a46 46 0 1 1-30 81L6 100l6-24A46 46 0 0 1 48 2z" fill="#ffffff"/>
      <circle cx="48" cy="48" r="40" fill="var(--office-icon)"/>
      <rect x="30" y="38" width="36" height="26" rx="3" fill="#ffffff"/>
      <path d="M40 38v-6h16v6" fill="none" stroke="#ffffff" stroke-width="4"/>
      <path d="M38 40v22M58 40v22" stroke="var(--office-icon)" stroke-width="2"/>
    </svg>
    <div class="flag__brand"><span class="flag__brand-dot"></span>TELVORA</div>
  </section>

  <section class="flag flag--shopping">
    <div class="flag__backdrop" role="img" aria-label="Warm orange bokeh light background"></div>
    <svg class="flag__curve" viewBox="0 0 236 1167"><path d="M26 300 Q34 50 200 0" fill="none" stroke="var(--curve)" stroke-width="2"/></svg>
    <p class="flag__message">You are<br>entering<br>Australia's<br>most<br>energy<br>efficient<br>shoping<br>centre.</p>
    <svg class="flag__icon" viewBox="0 0 96 104">
      <path d="M48 2a46 46 0 1 1-30 81L6 100l6-24A46 46 0 0 1 48 2z" fill="#ffffff"/>
      <circle cx="48" cy="48" r="40" fill="#ffffff"/>
      <path d="M26 34h7l6 22h22l5-16H36" fill="none" stroke="var(--shop-icon)" stroke-width="4" stroke-linejoin="round"/>
      <path d="M40 42v12M47 42v12M54 42v12" stroke="var(--shop-icon)" stroke-width="2"/>
      <circle cx="42" cy="63" r="3.5" fill="var(--shop-icon)"/>
      <circle cx="58" cy="63" r="3.5" fill="var(--shop-icon)"/>
    </svg>
    <div class="flag__brand"><span class="flag__brand-dot"></span>TELVORA</div>
  </section>

  <section class="flag flag--hotel">
    <div class="flag__backdrop" role="img" aria-label="Dark purple background with pink light swirls"></div>
    <svg class="flag__curve" viewBox="0 0 236 1167"><path d="M26 300 Q34 50 200 0" fill="none" stroke="var(--curve)" stroke-width="2"/></svg>
    <p class="flag__message">You are<br>entering<br>Australia's<br>most<br>energy<br>efficient<br>hotel.</p>
    <svg class="flag__icon" viewBox="0 0 96 104">
      <path d="M48 2a46 46 0 1 1-30 81L6 100l6-24A46 46 0 0 1 48 2z" fill="#ffffff"/>
      <circle cx="48" cy="48" r="40" fill="var(--hotel-icon)"/>
      <circle cx="48" cy="50" r="14" fill="#ffffff"/>
      <path d="M25 32v12M22 32v8q3 4 6 0v-8M25 44v20" stroke="#ffffff" stroke-width="3" fill="none" stroke-linecap="round"/>
      <path d="M71 32q-6 8 0 16v16" stroke="#ffffff" stroke-width="4" fill="none" stroke-linecap="round"/>
    </svg>
    <div class="flag__brand"><span class="flag__brand-dot"></span>TELVORA</div>
  </section>

</main>
</body>
</html>
```